Marlowe Consulting Cover 2 - Bright Ledger

Marlowe Consulting is a business consulting firm. We will publish a series of four thought leadership pieces online and via PDF. The second of the series is attached to this project. We need an eye-catching cover page with a back page that keeps with our branding. The document attached is in the final draft, and the cover and pack pages are placeholders only. You can find more about our branding and style on our website www.marloweconsulting.com.au. The other three projects can be found here with a similar brief, and you are welcome to submit a design for all 4.

```html
<!DOCTYPE html>
<html lang="en">
<head>
<meta charset="utf-8">
<title>Marlowe Consulting – Bright Ledger Cover and Back Page</title>
<link rel="stylesheet" href="https://fonts.googleapis.com/css2?family=League+Gothic&family=Catamaran:wght@400;500;700;800&display=swap">
<style>
  :root {
    --canvas: #e8e8e8;
    --orange: #f7941d;
    --blue: #00aeef;
    --blue-deep: #0098d4;
    --ink: #1c1c1c;
    --charcoal: #3a3a3b;
    --white: #ffffff;
  }
  * { margin: 0; padding: 0; box-sizing: border-box; }
  html, body { width: 1200px; height: 870px; overflow: hidden; background: var(--canvas); }
  body { position: relative; font-family: "Catamaran", sans-serif; }

  .page { position: absolute; top: 70px; width: 519px; height: 735px; overflow: hidden; }
  .page--cover { left: 58px; }
  .page--back { left: 612px; }

  .photo { position: absolute; top: 0; left: 0; width: 323px; height: 100%; }
  .page--cover .photo { background: linear-gradient(160deg, #ffffff 0%, #f4f7f9 45%, #e6ecef 75%, #f2f4f5 100%); }
  .page--back .photo { background: linear-gradient(170deg, #3b3b3c 0%, #383839 55%, #2e2e2f 100%); }

  .pattern-band { position: absolute; top: 0; left: 323px; width: 196px; height: 100%;
    background: linear-gradient(135deg, var(--blue) 0%, var(--blue-deep) 50%, var(--blue) 100%); }

  .brand { position: absolute; top: 62px; left: 36px; display: flex; align-items: center; gap: 10px; }
  .brand-dot { width: 44px; height: 44px; border-radius: 50%; background: var(--orange); }
  .brand-name { font-weight: 700; font-size: 20px; line-height: 20px; color: var(--orange); width: 120px; }

  .headline { position: absolute; top: 147px; left: 34px; width: 275px; white-space: nowrap;
    font-family: "League Gothic", sans-serif; font-weight: 400;
    font-size: 66px; line-height: 59px; color: var(--orange); text-transform: uppercase; }
  .headline .accent { color: var(--blue); }

  .accent-rule { position: absolute; left: 43px; top: 401px; width: 2px; height: 280px; background: var(--orange); }
  .cover-url { position: absolute; left: 42px; top: 688px; font-weight: 700; font-size: 16px; color: var(--ink); }

  .callout { position: absolute; left: 30px; top: 176px; color: var(--white); font-size: 17px;
    line-height: 22.5px; font-weight: 500; text-transform: uppercase; }
  .callout strong { color: var(--orange); font-weight: 800; }
  .callout-rule { position: absolute; left: 31px; top: 278px; width: 40px; height: 2px; background: var(--white); }

  .contact { position: absolute; left: 31px; color: var(--white); font-size: 11.5px; line-height: 15px; }
  .contact--first { top: 313px; }
  .contact--second { top: 403px; left: 34px; }
  .contact-name { color: var(--blue); font-weight: 800; font-size: 18px; line-height: 20px; }
  .contact-role { color: var(--orange); font-size: 11.5px; margin-bottom: 5px; }
  .contact b { font-weight: 800; }

  .follow { position: absolute; left: 34px; top: 576px; display: flex; align-items: center; gap: 4px;
    color: var(--white); font-size: 17px; }
  .social-dot { width: 18px; height: 18px; border-radius: 50%; background: var(--blue); }
  .social-dot--alt { background: var(--white); }
  .back-url { position: absolute; left: 34px; top: 598px; color: var(--orange); font-weight: 800; font-size: 15.5px; }
</style>
</head>
<body>
  <section class="page page--cover">
    <div class="photo" role="img" aria-label="Pale low-angle photograph of city office towers and a street lamp"></div>
    <div class="pattern-band" role="img" aria-label="Blue geometric maze-line brand pattern"></div>
    <div class="brand"><span class="brand-dot"></span><span class="brand-name">Marlowe Consulting</span></div>
    <h1 class="headline">Chasing<br>cash like<br>Toby <span class="accent">chases</span><br><span class="accent">the Wizzle</span></h1>
    <div class="accent-rule"></div>
    <p class="cover-url">marloweconsulting.com.au</p>
  </section>

  <section class="page page--back">
    <div class="photo" role="img" aria-label="Dark low-angle photograph of a city office tower"></div>
    <div class="pattern-band" role="img" aria-label="Blue geometric maze-line brand pattern"></div>
    <div class="brand"><span class="brand-dot"></span><span class="brand-name">Marlowe Consulting</span></div>
    <p class="callout">Contact us to find out<br>how Marlowe Consulting can<br>help build your company into<br>a market <strong>leader today.</strong></p>
    <div class="callout-rule"></div>
    <div class="contact contact--first">
      <p class="contact-name">Henry Marlowe</p>
      <p class="contact-role">Managing Director</p>
      <p><b>Mobile</b> +61 400 555 018</p>
      <p><b>Email</b> henry@marloweconsulting.com.au</p>
    </div>
    <div class="contact contact--second">
      <p class="contact-name">Oliver Marlowe</p>
      <p class="contact-role">Managing Director</p>
      <p><b>Mobile</b> +61 400 555 027</p>
      <p><b>Email</b> oliver@marloweconsulting.com.au</p>
    </div>
    <div class="follow">Follow <span class="social-dot"></span><span class="social-dot social-dot--alt"></span></div>
    <p class="back-url">marloweconsulting.com.au</p>
  </section>
</body>
</html>
```